National Virtual accounting firm needs website designed

I need a wordpress website design for a national virtual accounting firm. I will upload my business card, logo, and postcards that I have had designed and followed the same style. I want a similar style to be followed so I can keep the running theme similar.

Services include:

Tax Services:
Tax preparation and planning services for Individuals, businesses, estates, and nonprofits
Full Service Payroll for Businesses
ODV Audit Representation

Consulting:
Entity Selection & Restructuring
Financial Projections & Forecasts
Retirement Planning
IPO Readiness

Accounting:
Bookkeeping
Reviews and Compilations
Payroll Services

Other Services:
CFO Services
Compliance Services
Controller Services
Software Implementations for Brimlane, Corvanta, and Plivorn.

Target Market(s)

small to medium size businesses, and individuals

Industry/Entity Type

accounting firms

Font styles to use
Sans Serif

Colors
59FF00
82FF00
B8FF75
E3FFCB
F4FFEA

Requirements
Must have
• Color schematics from the logo and post cards/business cards

```html
<!DOCTYPE html>
<html lang="en">
<head>
<meta charset="utf-8">
<title>Verdano Accounting</title>
<link href="https://fonts.googleapis.com/css2?family=Montserrat:wght@500;600;700&family=Poppins:wght@300;400;500;600&display=swap" rel="stylesheet">
<style>
:root{
  --green:#5cb846;
  --green-dark:#4aa63a;
  --lime:#8dc63f;
  --yellow:#f6c500;
  --ink:#1d1d1d;
  --muted:#8a8a8a;
  --faint:#b5b5b5;
  --line:#e8e8e8;
  --paper:#ffffff;
  --soft:#f7f8f6;
  --field:#f1f1f1;
}
*{margin:0;padding:0;box-sizing:border-box}
html,body{width:1200px;height:4118px;overflow:hidden}
body{font-family:"Poppins",sans-serif;color:var(--ink);background:var(--paper);position:relative}
h1,h2,h3,h4,.display{font-family:"Montserrat",sans-serif;font-weight:600;letter-spacing:.5px}
.abs{position:absolute}
.btn{display:inline-flex;align-items:center;justify-content:center;border-radius:30px;font-family:"Montserrat",sans-serif;font-weight:700;font-size:11px;letter-spacing:1px;text-transform:uppercase;color:#fff;background:linear-gradient(90deg,var(--green),var(--lime));box-shadow:0 6px 14px rgba(92,184,70,.3)}

/* top bar */
.topbar{top:0;left:0;width:1200px;height:30px;background:var(--green);overflow:hidden}
.topbar .accent{position:absolute;top:0;left:720px;width:500px;height:30px;background:var(--yellow);transform:skewX(-35deg);transform-origin:bottom}
.topbar .item{position:absolute;top:0;height:30px;display:flex;align-items:center;gap:10px;font-size:10px;color:#fff}
.topbar .ring{width:16px;height:16px;border:1px solid rgba(255,255,255,.7);border-radius:50%}
.topbar .social{position:absolute;right:90px;top:8px;display:flex;gap:4px}
.topbar .social span{width:14px;height:14px;border:1.5px solid var(--ink);border-radius:50%}

/* nav */
.nav{top:30px;left:0;width:1200px;height:69px;background:#fff;box-shadow:0 2px 8px rgba(0,0,0,.05)}
.brand{display:flex;align-items:center;gap:8px;font-family:"Montserrat",sans-serif;font-weight:700;font-size:22px;color:var(--ink);letter-spacing:1px}
.brand .dot{width:20px;height:20px;border-radius:50%;background:var(--yellow)}
.nav .brand{position:absolute;left:102px;top:20px}
.nav ul{position:absolute;left:563px;top:29px;display:flex;gap:29px;list-style:none;font-size:10px;color:#333}
.nav ul li.active{color:var(--green)}
.nav .call{position:absolute;left:927px;top:20px;width:188px;height:33px;font-size:13px;gap:10px}

/* hero */
.hero{top:99px;left:0;width:1200px;height:582px;background:linear-gradient(100deg,#f2f2f2 0%,#e8e9ea 40%,#c9cdd2 70%,#dfe2e4 100%)}
.hero h1{position:absolute;left:102px;top:195px;font-size:48px;line-height:56px;font-weight:600;color:#111}
.hero .btn{position:absolute;left:102px;top:353px;width:202px;height:33px}
.hero .video{position:absolute;left:326px;top:353px;display:flex;align-items:center;gap:18px;font-size:12px;color:#444}
.hero .play{width:34px;height:34px;border-radius:50%;background:rgba(246,197,0,.25);display:flex;align-items:center;justify-content:center}
.hero .play i{width:18px;height:18px;border-radius:50%;background:var(--yellow);display:block}

/* about */
.about{top:681px;left:0;width:1200px;height:575px;background:#fff}
.about .frame{position:absolute;left:144px;top:59px;width:410px;height:394px;background:var(--yellow)}
.photo{background:linear-gradient(135deg,#e9ecef,#b9c3cc)}
.about .p1{position:absolute;left:157px;top:73px;width:409px;height:218px}
.about .p2{position:absolute;left:157px;top:305px;width:216px;height:156px;background:linear-gradient(135deg,#dfe6ee,#8ea3c0)}
.about .p3{position:absolute;left:386px;top:305px;width:210px;height:212px;background:linear-gradient(135deg,#f1ede8,#c9b7a6)}
.about .eyebrow{position:absolute;left:663px;top:97px;font-size:14px;letter-spacing:1.5px;color:var(--green)}
.about h2{position:absolute;left:663px;top:131px;font-size:38px;line-height:41px;color:#111}
.about p{position:absolute;left:663px;top:244px;width:400px;font-size:11.5px;line-height:23px;color:#555}
.stats{position:absolute;left:663px;top:338px;display:flex}
.stat{padding-right:24px;margin-right:24px;border-right:1.5px solid #999}
.stat:last-child{border:0}
.stat b{display:block;font-family:"Montserrat",sans-serif;font-size:24px;font-weight:700;color:var(--green)}
.stat small{font-size:10px;letter-spacing:1px;color:#333}
.about .btn{position:absolute;left:663px;top:447px;width:132px;height:34px}

/* services */
.services{top:1256px;left:0;width:1200px;height:574px;background:linear-gradient(120deg,var(--green-dark) 0%,var(--green) 45%,var(--lime) 100%)}
.services h2{position:absolute;left:0;top:58px;width:1200px;text-align:center;color:#fff;font-size:42px;line-height:46px}
.card{position:absolute;top:206px;width:233px;height:216px;background:#fff;border-radius:4px;padding:24px 25px}
.card .icon{width:66px;height:72px;border-radius:8px;background:linear-gradient(135deg,#eef8e6,#d7efc4);border:2px solid var(--green)}
.card h4{margin-top:24px;font-family:"Poppins",sans-serif;font-weight:400;font-size:16px;letter-spacing:1px;color:#222}
.card p{margin-top:16px;font-size:10.5px;line-height:17px;color:#a4a4a4}
.services .more{position:absolute;left:514px;top:481px;width:173px;height:34px;border-radius:30px;background:#fff;color:var(--green);font-family:"Montserrat",sans-serif;font-weight:700;font-size:10px;letter-spacing:1px;display:flex;align-items:center;justify-content:center}

/* testimonials */
.testimonials{top:1830px;left:0;width:1200px;height:583px;background:#fff}
.section-title{position:absolute;left:0;width:1200px;text-align:center;font-size:40px;color:#111}
.section-sub{position:absolute;left:440px;width:320px;text-align:center;font-size:11px;line-height:18px;color:#999}
.quote{position:absolute;top:228px;width:310px;height:197px;background:#fff;box-shadow:0 4px 18px rgba(0,0,0,.09);text-align:center;overflow:hidden}
.quote .corner{position:absolute;right:0;top:0;width:58px;height:58px;background:linear-gradient(225deg,var(--yellow) 50%,transparent 50%)}
.quote h4{margin-top:40px;font-family:"Poppins",sans-serif;font-weight:500;font-size:17px;color:#111}
.quote .role{font-size:12px;color:#aaa}
.quote p{margin:18px auto 0;width:260px;font-size:11px;line-height:19px;color:#aaa}
.avatar{position:absolute;top:201px;width:54px;height:54px;border-radius:50%;background:linear-gradient(135deg,#e5e0da,#9a8d80);border:3px solid #fff}
.arrow{position:absolute;top:483px;width:52px;height:44px;background:#e7f5df;display:flex;align-items:center;justify-content:center}

/* team */
.team{top:2413px;left:0;width:1200px;height:647px;background:var(--soft)}
.team h2 span{color:var(--green)}
.member{position:absolute;top:217px;width:256px;text-align:center}
.member .shot{height:302px;background:linear-gradient(160deg,#d9dcdc,#6f7572)}
.member h4{margin-top:22px;font-family:"Poppins",sans-serif;font-weight:500;font-size:21px;color:#111}
.member small{display:block;margin-top:6px;font-size:11px;color:#999}

/* contact */
.contact{top:3060px;left:0;width:1200px;height:622px;background:linear-gradient(110deg,#55784a 0%,#3e6a38 50%,#2e5a2f 100%)}
.contact h2{position:absolute;left:130px;top:143px;font-size:40px;color:#fff}
.contact .intro{position:absolute;left:130px;top:200px;width:300px;font-size:11px;line-height:18px;color:#dfe8dc}
.cline{position:absolute;left:130px;display:flex;align-items:flex-start;gap:25px;color:#fff;font-family:"Montserrat",sans-serif;font-size:18px;letter-spacing:1px;line-height:20px}
.cline .ic{flex:none;width:34px;height:34px;border-radius:50%;background:var(--green);display:flex;align-items:center;justify-content:center;margin-top:-6px}
.form{position:absolute;left:578px;top:69px;width:453px;height:485px;background:#fff;padding:32px 37px}
.form h3{font-size:26px;color:#111}
.form .row{display:flex;gap:14px;margin-top:18px}
.form label{display:block;font-size:11px;letter-spacing:.5px;color:#666;margin-bottom:8px}
.form .field{width:183px;height:38px;background:var(--field);font-size:10px;color:#bbb;padding:12px 16px}
.form .field.wide{width:380px;height:104px}
.form .btn{margin-top:26px;width:380px;height:36px;font-size:10px}

/* footer */
.footer{top:3682px;left:0;width:1200px;height:436px;background:linear-gradient(110deg,var(--lime) 0%,var(--green) 100%);color:#fff}
.footer .brand{position:absolute;left:102px;top:104px;color:#fff}
.footer .brand .dot{background:#fff}
.footer .about-text{position:absolute;left:102px;top:171px;width:260px;font-size:11px;line-height:19px}
.footer .social{position:absolute;left:102px;top:290px;display:flex;gap:10px}
.footer .social span{width:30px;height:30px;border:1.5px solid #fff;border-radius:50%}
.fcol{position:absolute;top:117px}
.fcol h4{font-family:"Poppins",sans-serif;font-weight:500;font-size:17px;margin-bottom:20px}
.fcol ul{list-style:none;font-size:11px;line-height:24px}
.fcol .gi{display:flex;align-items:center;gap:10px}
.fcol .gi i{width:16px;height:16px;border:1px solid #fff;border-radius:50%;display:block}
.footer .rule{position:absolute;left:102px;top:354px;width:996px;height:1px;background:rgba(255,255,255,.5)}
.footer .copy{position:absolute;left:102px;top:385px;font-size:10px}
.footer .legal{position:absolute;right:102px;top:385px;font-size:10px}
</style>
</head>
<body>

<div class="abs topbar">
  <div class="accent"></div>
  <div class="item" style="left:102px"><span class="ring"></span>Call: 026410759</div>
  <div class="item" style="left:255px"><span class="ring"></span>Mail: hello@verdano.example</div>
  <div class="item" style="left:448px"><span class="ring"></span>Via Lorenta 14, 20100 Corsano</div>
  <div class="social"><span></span><span></span><span></span></div>
</div>

<header class="abs nav">
  <div class="brand"><span class="dot"></span>VERDANO</div>
  <ul>
    <li class="active">HOME</li><li>ABOUT US</li><li>SERVICES</li><li>CONTACT</li><li>BLOG</li>
  </ul>
  <div class="btn call">
    <svg width="14" height="14" viewBox="0 0 24 24" fill="none" stroke="#fff" stroke-width="2"><path d="M22 16.9v3a2 2 0 0 1-2.2 2 19.8 19.8 0 0 1-8.6-3.1 19.5 19.5 0 0 1-6-6A19.8 19.8 0 0 1 2.1 4.2 2 2 0 0 1 4.1 2h3a2 2 0 0 1 2 1.7c.1 1 .4 1.9.7 2.8a2 2 0 0 1-.5 2.1L8 9.9a16 16 0 0 0 6 6l1.3-1.3a2 2 0 0 1 2.1-.4c.9.3 1.8.6 2.8.7a2 2 0 0 1 1.7 2z"/></svg>
    512-555-0148
  </div>
</header>

<section class="abs hero" role="img" aria-label="Photo of two colleagues reviewing work at a computer in a bright office">
  <h1>Financial Planning<br>Of Your Business</h1>
  <div class="btn">Request a call back</div>
  <div class="video"><span class="play"><i></i></span>Watch the video</div>
</section>

<section class="abs about">
  <div class="frame"></div>
  <div class="p1 photo" role="img" aria-label="Photo of hands reviewing financial charts with a calculator"></div>
  <div class="p2" role="img" aria-label="Photo of a hand marking a bar chart report"></div>
  <div class="p3" role="img" aria-label="Photo of two businesswomen at an office desk"></div>
  <div class="eyebrow">WHO WE ARE</div>
  <h2>Verdano<br>Accounting Firm</h2>
  <p>Lorem Ipsum is simply dummy text of the printing and typesetting industry. Lorem Ipsum has been the industry's standard dummy text ever since the 1500s</p>
  <div class="stats">
    <div class="stat"><b>700+</b><small>PROJECT DONE</small></div>
    <div class="stat"><b>100%</b><small>SUCCESS RATE</small></div>
    <div class="stat"><b>20+</b><small>YEARS EXPERIENCE</small></div>
  </div>
  <div class="btn">Read more</div>
</section>

<section class="abs services">
  <h2>Best Accounting<br>Services</h2>
  <div class="card" style="left:99px"><div class="icon" role="img" aria-label="Tax form and calculator icon"></div><h4>Tax Services</h4><p>Lorem Ipsum is simply dummy text of the printing and typesetting industry.</p></div>
  <div class="card" style="left:355px"><div class="icon" role="img" aria-label="Consulting people and gear icon"></div><h4>Consulting</h4><p>Lorem Ipsum is simply dummy text of the printing and typesetting industry.</p></div>
  <div class="card" style="left:609px"><div class="icon" role="img" aria-label="Accounting calculator and ledger icon"></div><h4>Accounting</h4><p>Lorem Ipsum is simply dummy text of the printing and typesetting industry.</p></div>
  <div class="card" style="left:865px"><div class="icon" role="img" aria-label="CFO dashboard screen icon"></div><h4>CFO Services</h4><p>Lorem Ipsum is simply dummy text of the printing and typesetting industry.</p></div>
  <div class="more">SEE ALL SERVICES</div>
</section>

<section class="abs testimonials">
  <h2 class="section-title" style="top:56px">Client Testimonials</h2>
  <p class="section-sub" style="top:124px">Lorem Ipsum is simply dummy text of the printing and typesetting industry.</p>
  <div class="quote" style="left:110px"><div class="corner"></div><h4>Owen Marsh</h4><div class="role">Ceo and founder</div><p>Lorem ipsum dolor sit amet, consetetur sadipscing elitr, sed diam nonumy eirmodLorem ipsum dolor sit amet, consetetur sadipscing elitr,</p></div>
  <div class="quote" style="left:446px"><div class="corner"></div><h4>Liam Decker</h4><div class="role">Ceo and founder</div><p>Lorem ipsum dolor sit amet, consetetur sadipscing elitr, sed diam nonumy eirmodLorem ipsum dolor sit amet, consetetur sadipscing elitr,</p></div>
  <div class="quote" style="left:780px"><div class="corner"></div><h4>Ethan Vale</h4><div class="role">Ceo and founder</div><p>Lorem ipsum dolor sit amet, consetetur sadipscing elitr, sed diam nonumy eirmodLorem ipsum dolor sit amet, consetetur sadipscing elitr,</p></div>
  <div class="avatar" style="left:238px" role="img" aria-label="Client portrait"></div>
  <div class="avatar" style="left:573px" role="img" aria-label="Client portrait"></div>
  <div class="avatar" style="left:908px" role="img" aria-label="Client portrait"></div>
  <div class="arrow" style="left:544px"><svg width="14" height="14" viewBox="0 0 24 24" fill="none" stroke="#5cb846" stroke-width="3"><path d="M15 4l-8 8 8 8"/></svg></div>
  <div class="arrow" style="left:603px"><svg width="14" height="14" viewBox="0 0 24 24" fill="none" stroke="#5cb846" stroke-width="3"><path d="M9 4l8 8-8 8"/></svg></div>
</section>

<section class="abs team">
  <h2 class="section-title" style="top:56px">Meet Our <span>Accountants</span></h2>
  <p class="section-sub" style="top:126px">Lorem Ipsum is simply dummy text of the printing and typesetting industry.</p>
  <div class="member" style="left:161px"><div class="shot" role="img" aria-label="Portrait of an accountant in a light suit outdoors"></div><h4>Grant Ellery</h4><small>Ceo and Founder</small></div>
  <div class="member" style="left:455px"><div class="shot" role="img" aria-label="Portrait of an accountant in glasses and a dark hoodie"></div><h4>Noah Brandt</h4><small>Ceo and Founder</small></div>
  <div class="member" style="left:749px"><div class="shot" style="background:linear-gradient(160deg,#f4f4f4,#8a8f94)" role="img" aria-label="Portrait of an accountant in a dark suit"></div><h4>Miles Carden</h4><small>Ceo and Founder</small></div>
</section>

<section class="abs contact" role="img" aria-label="Green tinted photo of hands working at a laptop">
  <h2>Contact Us</h2>
  <p class="intro">Lorem Ipsum is simply dummy text of the printing and typesetting industry.</p>
  <div class="cline" style="top:280px"><span class="ic"><svg width="14" height="14" viewBox="0 0 24 24" fill="none" stroke="#fff" stroke-width="2"><path d="M22 16.9v3a2 2 0 0 1-2.2 2 19.8 19.8 0 0 1-8.6-3.1 19.5 19.5 0 0 1-6-6A19.8 19.8 0 0 1 2.1 4.2 2 2 0 0 1 4.1 2h3a2 2 0 0 1 2 1.7c.1 1 .4 1.9.7 2.8a2 2 0 0 1-.5 2.1L8 9.9a16 16 0 0 0 6 6l1.3-1.3a2 2 0 0 1 2.1-.4c.9.3 1.8.6 2.8.7a2 2 0 0 1 1.7 2z"/></svg></span>Call: +414-555-0192</div>
  <div class="cline" style="top:340px"><span class="ic"><svg width="14" height="14" viewBox="0 0 24 24" fill="none" stroke="#fff" stroke-width="2"><rect x="3" y="5" width="18" height="14" rx="2"/><path d="M3 7l9 6 9-6"/></svg></span>Email:info@verdano.example</div>
  <div class="cline" style="top:399px"><span class="ic"><svg width="14" height="14" viewBox="0 0 24 24" fill="none" stroke="#fff" stroke-width="2"><path d="M12 22s7-7 7-12a7 7 0 0 0-14 0c0 5 7 12 7 12z"/><circle cx="12" cy="10" r="2.5"/></svg></span>Via Lorenta 14,<br>20100 Corsano</div>
  <div class="form">
    <h3>Request A Call Back</h3>
    <div class="row">
      <div><label>First Name*</label><div class="field">First Name</div></div>
      <div><label>Last Name*</label><div class="field">Last Name</div></div>
    </div>
    <div class="row">
      <div><label>Email Address*</label><div class="field">Email Address</div></div>
      <div><label>Phone Number*</label><div class="field">Phone Number</div></div>
    </div>
    <div class="row"><div><label>Message</label><div class="field wide">Message</div></div></div>
    <div class="btn">Send message</div>
  </div>
</section>

<footer class="abs footer">
  <div class="brand"><span class="dot"></span>VERDANO</div>
  <p class="about-text">Lorem ipsum dolor sit amet, consetetur sadipscing elitr, sed diam nonumy eirmodLorem ipsum dolor sit amet, consetetur sadipscing elitr, sed diam</p>
  <div class="social"><span></span><span></span><span></span></div>
  <div class="fcol" style="left:475px"><h4>Quick Links</h4><ul><li>Home</li><li>About</li><li>Services</li><li>Blog</li><li>Contact</li></ul></div>
  <div class="fcol" style="left:708px"><h4>Services</h4><ul><li>Financial Models</li><li>Budgeting Process</li><li>Temporary Staffing</li><li>Data Cleansing</li></ul></div>
  <div class="fcol" style="left:951px"><h4>Get In Touch</h4><ul>
    <li class="gi"><i></i>Call: +414-555-0192</li>
    <li class="gi"><i></i>Fax: +414-555-0177</li>
    <li class="gi"><i></i>Email: info@verdano.example</li>
  </ul></div>
  <div class="rule"></div>
  <div class="copy">© 2002-2015 Verdano All rights reserved</div>
  <div class="legal">Site map &nbsp;|&nbsp; Terms and conditions &nbsp;|&nbsp; Privacy Policy</div>
</footer>

</body>
</html>
```